Create a Graphic About YOURSELF and PixelHarbor

PixelHarbor would like you (designers) to create an awesome graphic to promote YOURSELF and your profile on PixelHarbor!

Your graphic should communicate your name, your services and should mention PixelHarbor.

The design should be perfect for sharing on Chatterly. Here's an example of what we'd like http://blog.pixelharbor-example.ca/article/333/pixelharbor-launches-3000-hire-me-social-design-contest

Once you submitted your design, we'd love you to share the design ('advertisement') and promote yourself and PixelHarbor to your friends and potential customers. So make your submissions great and get your friends to vote for your design by 'Liking' it on Chatterly!

Prizes:
$1500 - "PixelHarbor Community" prize awarded to the designer with the most Chatterly 'Likes'
5 x $50 for the next 5 'most liked' designs on Chatterly

$1000 - "Hire Me" prize awarded to the designer who receives the most client invites
5 x $50 for the next 5 'most invited' designers

In summary, this is a great opportunity for you to increase your exposure to PixelHarbor customers and win cash prizes. Show off your design skills and get hired by PixelHarbor customers from around the world!

Target Market(s)

Fans, friends and customers of YOU

Industry/Entity Type

Cash

Requirements
Must have
• 1) Include your PixelHarbor user name on the graphic so customers can find you in the PixelHarbor Designer Directory
2) Include the tagline "Hire Me on PixelHarbor.com!" in your graphic design.
3) Share your design's URL on our Chatterly wall at http://chatterly-example.com/pixelharbor and get your friends to 'like' your design.
Nice to have
• 1) Include a tagline that expresses your design approach/philosophy
2) Artwork dimensions: 403 x 403 px
3) You can submit more than 1 design!
Should not have
• You must own the copyright of any images you use including stock imagery.

```html
<!DOCTYPE html>
<html lang="en">
<head>
<meta charset="utf-8">
<title>Hire Me – JxHale for graphic design</title>
<link rel="stylesheet" href="https://fonts.googleapis.com/css2?family=Chewy&family=Saira+Extra+Condensed:wght@700&family=Quicksand:wght@300&family=Open+Sans:wght@600&display=swap">
<style>
  :root {
    --wood-dark: #141010;
    --wood-warm: #6a3f16;
    --glow-orange: #ff7a00;
    --headline-top: #ffd21a;
    --headline-bottom: #ff7f00;
    --headline-edge: #6b1a05;
    --emboss-fill: #3a2e24;
    --emboss-edge: #1e1712;
    --tagline: #a07a52;
    --at-line: #1a6a98;
    --brand-ink: #0e0c0b;
    --brand-dot: #1a78ad;
  }
  html, body {
    margin: 0;
    padding: 0;
    width: 1200px;
    height: 967px;
    overflow: hidden;
    background: var(--wood-dark);
  }
  .poster {
    position: relative;
    width: 1200px;
    height: 967px;
  }
  .poster svg { display: block; }
  .hire-me {
    font-family: "Chewy", "Comic Sans MS", cursive;
    font-size: 72px;
    letter-spacing: 8px;
  }
  .username {
    font-family: "Saira Extra Condensed", "Arial Narrow", sans-serif;
    font-weight: 700;
    font-size: 420px;
  }
  .service {
    font-family: "Quicksand", "Helvetica Neue", sans-serif;
    font-weight: 300;
    font-size: 29px;
    letter-spacing: 2px;
  }
  .brand-name {
    font-family: "Open Sans", "Helvetica Neue", sans-serif;
    font-weight: 600;
    font-size: 62px;
  }
</style>
</head>
<body>
<main class="poster">
  <svg width="1200" height="967" viewBox="0 0 1200 967" xmlns="http://www.w3.org/2000/svg">
    <defs>
      <linearGradient id="woodBase" x1="0" y1="0" x2="1" y2="0">
        <stop offset="0" stop-color="#171312"/>
        <stop offset="0.45" stop-color="#2b2119"/>
        <stop offset="1" stop-color="#2a1c10"/>
      </linearGradient>
      <radialGradient id="warmLight" cx="0.72" cy="0.5" r="0.45">
        <stop offset="0" stop-color="#6a3f16" stop-opacity="0.85"/>
        <stop offset="1" stop-color="#6a3f16" stop-opacity="0"/>
      </radialGradient>
      <radialGradient id="vignette" cx="0.55" cy="0.5" r="0.75">
        <stop offset="0.55" stop-color="#000" stop-opacity="0"/>
        <stop offset="1" stop-color="#000" stop-opacity="0.7"/>
      </radialGradient>
      <linearGradient id="headlineFill" x1="0" y1="0" x2="0" y2="1">
        <stop offset="0" stop-color="#ffd21a"/>
        <stop offset="1" stop-color="#ff7f00"/>
      </linearGradient>
      <filter id="orangeGlow" x="-20%" y="-40%" width="140%" height="180%">
        <feGaussianBlur in="SourceAlpha" stdDeviation="7" result="soft"/>
        <feFlood flood-color="#ff7a00" flood-opacity="0.9" result="tint"/>
        <feComposite in="tint" in2="soft" operator="in" result="halo"/>
        <feMerge><feMergeNode in="halo"/><feMergeNode in="SourceGraphic"/></feMerge>
      </filter>
      <filter id="blueGlow" x="-20%" y="-20%" width="140%" height="140%">
        <feGaussianBlur in="SourceGraphic" stdDeviation="4" result="soft"/>
        <feMerge><feMergeNode in="soft"/><feMergeNode in="SourceGraphic"/></feMerge>
      </filter>
      <filter id="brandGlow" x="-10%" y="-30%" width="120%" height="160%">
        <feDropShadow dx="0" dy="0" stdDeviation="4" flood-color="#ff7a00" flood-opacity="0.5"/>
      </filter>
      <path id="headlineArc" d="M 78 352 Q 150 120 480 112"/>
      <mask id="atOutline" maskUnits="userSpaceOnUse" x="0" y="0" width="1200" height="967">
        <g fill="none" stroke-linecap="round">
          <g stroke="#fff" stroke-width="28">
            <path class="at-stroke" d="M 355 928 A 143 143 0 1 1 452 810 Q 440 858 408 860 Q 391 858 391 838 L 391 760"/>
            <circle cx="337" cy="795" r="52"/>
          </g>
          <g stroke="#000" stroke-width="24">
            <path d="M 355 928 A 143 143 0 1 1 452 810 Q 440 858 408 860 Q 391 858 391 838 L 391 760"/>
            <circle cx="337" cy="795" r="52"/>
          </g>
        </g>
      </mask>
    </defs>

    <g class="background" role="img" aria-label="Dark wooden floorboard texture with a warm amber light">
      <rect width="1200" height="967" fill="url(#woodBase)"/>
      <rect width="1200" height="967" fill="url(#warmLight)"/>
      <rect width="1200" height="967" fill="url(#vignette)"/>
    </g>

    <g class="username-emboss" transform="translate(148 0) skewX(-14)">
      <text class="username" x="150" y="593" textLength="950" lengthAdjust="spacingAndGlyphs"
            fill="var(--emboss-fill)" fill-opacity="0.55"
            stroke="var(--emboss-edge)" stroke-width="5" stroke-opacity="0.7">JxHale</text>
    </g>

    <g class="headline" filter="url(#orangeGlow)">
      <text class="hire-me" fill="url(#headlineFill)" stroke="var(--headline-edge)" stroke-width="3"
            paint-order="stroke">
        <textPath href="#headlineArc">hire ME</textPath>
      </text>
    </g>

    <text class="service" x="139" y="623" fill="var(--tagline)">for graphic design</text>

    <g class="at-sign" filter="url(#blueGlow)">
      <rect x="140" y="620" width="340" height="340" fill="var(--at-line)" mask="url(#atOutline)"/>
    </g>

    <g class="brand" filter="url(#brandGlow)">
      <circle cx="553" cy="791" r="32" fill="var(--brand-dot)"/>
      <text class="brand-name" x="602" y="813" textLength="550" lengthAdjust="spacingAndGlyphs" fill="var(--brand-ink)">PixelHarbor.com</text>
    </g>
  </svg>
</main>
</body>
</html>
```